Web design for Marketplace

Guys!
1st of all, thank you for willing to help me out.
I have attached PDF file with examples.
I am looking for professional and clean design for my new project “ Lantern of Seers “. Its marketplace for Psychic Readers around the world. Where they will able to register to provide their services via Chat,Email and sell their products on their personal stores.
Customer will able to get services and buy products from Psychic on Marketplace.
url : http://www.lanternofseers-demo.net
Please note: it doesn’t matter, what my current site looks like. I am looking for completely new design.
It doesn't matter if you add or remove : Vidlume video or even text which is on the home page in new design.
Following are the main pages of the website, which i am looking to be design.
1. Home page
2. Psychic
3. Marketplace
4. Psychic profile page
5. Psychic Store page
6. Psychic product page
7. Logo
following is the website, which i like the most. I would love to have something like that. It is neat , clean and friendly. I am looking for depth in design and neatness and borders (matter and a lot and it should be prefect ).
http://www.craftnook-demo.net
P.S : i believe it will be helpful to choose one of you. If you can only create design of " Homepage" at 1st , so i can go ahead and hire one of you guys.
Best,
Hi guys!
Guys,

```html
<!DOCTYPE html>
<html lang="en">
<head>
<meta charset="utf-8">
<title>Lantern of Seers – Home</title>
<link rel="stylesheet" href="https://fonts.googleapis.com/css2?family=PT+Sans:ital,wght@0,400;0,700;1,400;1,700&family=PT+Sans+Narrow:wght@400;700&display=swap">
<style>
:root{
  --orange:#f05a0e;
  --orange-deep:#e24f0a;
  --orange-light:#f7941d;
  --ink:#1e1e1e;
  --text:#6b6b6b;
  --muted:#8a8a8a;
  --panel:#f1f1f1;
  --card:#ffffff;
  --line:#e3e3e3;
  --pill:#e6e6e6;
}
*{box-sizing:border-box;margin:0;padding:0}
html,body{width:919px;height:1200px;overflow:hidden;background:#fff}
body{font-family:"PT Sans",sans-serif;color:var(--text);position:relative}
.page{position:relative;width:919px;height:1200px;overflow:hidden;background:#fff}
.abs{position:absolute}

/* header */
.brand{left:102px;top:22px}
.brand-name{display:flex;align-items:center;gap:6px;font-family:"PT Sans",sans-serif;font-weight:700;font-size:19px;color:var(--ink);line-height:1}
.brand-name i{display:block;width:12px;height:12px;background:var(--orange)}
.brand-tag{font-size:14px;color:var(--ink);margin-top:8px;letter-spacing:.2px}
.top-links{left:600px;top:16px;display:flex;align-items:center;font-size:13px}
.btn-signin{background:var(--ink);color:#fff;border-radius:5px;width:66px;height:26px;display:flex;align-items:center;justify-content:center}
.top-links a{color:var(--orange);text-decoration:none;margin-left:24px}
.cart{left:646px;top:69px;width:178px;height:29px;background:#e4e4e4;border-radius:2px;display:flex;align-items:center;gap:6px;padding-left:12px;font-family:"PT Sans Narrow",sans-serif;font-weight:700;font-size:12px;color:#777}

/* nav */
.nav{left:76px;top:99px;width:766px;height:50px}
.nav ul{position:absolute;inset:0;list-style:none;display:flex;align-items:center;font-family:"PT Sans Narrow",sans-serif;font-size:15px;color:#fff}
.nav li{position:absolute;top:16px}

/* hero */
.hero{left:0;top:149px;width:919px;height:333px;background:radial-gradient(ellipse at 30% 40%,#fff 0%,#fafafa 55%,#ececec 100%)}
.hero-title{left:126px;top:219px;font-family:"PT Sans Narrow",sans-serif;font-weight:700;font-size:18px;color:var(--orange)}
.hero-copy{left:126px;top:254px;width:314px;font-size:9.6px;line-height:16.8px;color:var(--text);text-align:justify}
.hero-ask{left:146px;top:357px;font-family:"PT Sans Narrow",sans-serif;font-weight:700;font-size:20px;color:#666}
.btn-join{left:321px;top:354px;width:106px;height:24px;background:var(--ink);border-radius:3px;color:#fff;font-family:"PT Sans Narrow",sans-serif;font-weight:700;font-size:14px;display:flex;align-items:center;justify-content:center;gap:10px}
.btn-join span{width:13px;height:13px;border-radius:50%;background:#666;display:inline-block;position:relative}
.btn-join span::after{content:"";position:absolute;left:5px;top:4px;border-left:4px solid #fff;border-top:2.5px solid transparent;border-bottom:2.5px solid transparent}
.dots{left:102px;top:445px;display:flex;gap:6px}
.dots i{width:11px;height:11px;border-radius:50%;background:#cfcfcf;display:block}
.dots i:first-child{background:var(--orange)}
.hero-art{left:478px;top:172px;width:322px;height:310px;background:radial-gradient(circle at 50% 35%,#f7a21c 0%,#e8621a 40%,#2a2a2a 75%,#f5f5f5 100%);border-radius:40% 40% 0 0}

/* main panel */
.main{left:77px;top:482px;width:765px;height:642px;background:var(--panel)}
.intro-title{left:92px;top:494px;font-size:16px;color:var(--ink)}
.intro-copy{left:92px;top:518px;width:542px;font-size:9.6px;line-height:16.8px;color:var(--text)}
.btn-orange{background:linear-gradient(#fa9a2a,var(--orange-light) 50%,#f07c0c);color:#fff;border-radius:2px;font-family:"PT Sans",sans-serif;font-weight:700;font-size:10.5px;display:flex;align-items:center;justify-content:center}
.read-more{left:93px;top:600px;width:69px;height:23px}
.video{left:640px;top:494px;width:190px;height:146px;background:#d9cfd3;padding:4px}
.video-screen{position:relative;width:100%;height:100%;background:linear-gradient(135deg,#6a6058,#2c2a2a 70%,#1a1a1a)}
.video-play{position:absolute;left:76px;top:53px;width:34px;height:26px;background:#ddd;border-radius:4px;border:1px solid #999}
.video-play::after{content:"";position:absolute;left:12px;top:6px;border-left:11px solid #333;border-top:7px solid transparent;border-bottom:7px solid transparent}
.video-caption{position:absolute;left:0;right:0;bottom:8px;text-align:center;color:#eee;font-size:11px;font-weight:700}

/* cards */
.card{background:var(--card);border:3px solid #fbfbfb;box-shadow:0 0 0 1px var(--line),0 1px 3px rgba(0,0,0,.08)}
.card-head{position:absolute;left:16px;top:14px;font-size:11.5px;color:var(--ink);text-transform:uppercase}
.arrows{position:absolute;top:18px;right:20px;display:flex;gap:6px}
.arrows i,.products-arrows i{width:11px;height:11px;border-radius:50%;background:#eee;border:1px solid #ddd;display:block;position:relative}
.arrows i::after,.products-arrows i::after{content:"";position:absolute;top:3px;left:4px;border-left:3px solid #333;border-top:2px solid transparent;border-bottom:2px solid transparent}
.arrows i:first-child::after,.products-arrows i:first-child::after{left:3px;border-left:0;border-right:3px solid #333}
.entry{position:absolute;left:16px;width:232px;height:74px}
.entry p{width:139px;font-size:9.3px;line-height:13.6px;color:var(--text);text-align:justify}
.entry b{color:var(--orange);font-style:italic}
.entry .thumb{position:absolute;left:147px;top:0;width:84px;height:74px;border:3px solid #fff;box-shadow:0 0 0 1px #ddd,0 1px 3px rgba(0,0,0,.2)}
.view-more{position:absolute;left:82px;top:63px;width:56px;height:18px;border-radius:9px;background:var(--pill);color:var(--orange-light);font-size:9.5px;font-style:italic;display:flex;align-items:center;justify-content:center}

.side-title{position:absolute;left:16px;top:18px;font-family:"PT Sans Narrow",sans-serif;font-weight:700;font-size:15px;color:var(--orange-light)}
.side-copy{position:absolute;left:17px;top:42px;width:150px;font-size:9.4px;line-height:15px;color:var(--orange-deep)}
.side-input{position:absolute;left:17px;top:76px;width:146px;height:20px;border:1px solid #ddd;border-radius:2px;background:#fff}
.signup{position:absolute;left:18px;top:105px;width:62px;height:23px}
.side-note{position:absolute;left:17px;top:138px;font-size:9.4px;color:#555}
.item{position:absolute;top:48px;width:63px;height:97px;border:1px solid #ddd;background:#fff;text-align:center;font-size:8.8px}
.item .pic{margin:3px auto 0;width:46px;height:60px;background:radial-gradient(circle,#d24 0%,#5a0610 60%,#111 100%)}
.item .name{color:var(--orange-deep);margin-top:5px;line-height:11px}
.item .price{color:#444;font-size:8px;line-height:10px}

.products-title{left:90px;top:1001px;font-size:12px;color:var(--ink)}
.products-arrows{left:587px;top:1000px;display:flex;gap:5px}
.product{top:1024px;width:95px;height:84px;background:#fff;border:1px solid #e2e2e2;padding:3px}
.product div{width:100%;height:100%}

/* footer */
.footer{left:0;top:1124px;width:919px;height:76px;background:var(--orange-deep)}
.footer-links{left:84px;top:1140px;font-size:9.6px;color:#fff;display:flex;gap:7px}
.copyright{left:84px;top:1164px;font-size:9.6px;color:#fff}
.social{left:718px;top:1142px;display:flex;gap:10px}
.social i{display:block;width:22px;height:22px;border-radius:50%;background:#f37a3e}
.social svg{display:block}
</style>
</head>
<body>
<div class="page">

  <header>
    <div class="abs brand">
      <div class="brand-name"><i></i>Lantern of Seers</div>
      <div class="brand-tag">a world of psychics</div>
    </div>
    <div class="abs top-links">
      <span class="btn-signin">SIGN IN</span>
      <a href="#">HELP</a>
      <a href="#">JOIN NOW</a>
    </div>
    <div class="abs cart">
      <svg width="18" height="14" viewBox="0 0 18 14"><path d="M1 1h3l2 8h9l2-6H5" fill="none" stroke="#888" stroke-width="1.4"/><circle cx="7" cy="12" r="1.3" fill="#888"/><circle cx="14" cy="12" r="1.3" fill="#888"/></svg>
      MY CART - (0) ITEMS &nbsp;$00.00
    </div>
  </header>

  <nav class="abs nav">
    <svg width="766" height="50" viewBox="0 0 766 50"><polygon points="0,0 766,0 748,25 766,50 0,50 18,25" fill="#f05a0e"/></svg>
    <ul>
      <li style="left:24px">HOME</li>
      <li style="left:84px">PSYCHIC</li>
      <li style="left:158px">MARKETPLACE</li>
      <li style="left:266px">PSYCHIC PROFILE</li>
      <li style="left:390px">PSYCHIC STORE</li>
      <li style="left:503px">PSYCHIC PRODUCT</li>
      <li style="left:642px">MY ACCOUNT</li>
    </ul>
  </nav>

  <section class="abs hero"></section>
  <h1 class="abs hero-title">WELCOME TO LOS</h1>
  <p class="abs hero-copy">If you have an issue in your life that is causing you any sort of distress, no matter what it is, a reading from one of our psychics will give you immediate, compassionate insight. There are moments when &nbsp;you need more answers than you can get on your own. That's why the gifted psychics at Lantern of Seers are here for you, 24/7.</p>
  <div class="abs hero-ask">ARE YOU PSYCHIC?</div>
  <div class="abs btn-join">JOIN NOW <span></span></div>
  <div class="abs dots"><i></i><i></i><i></i><i></i></div>
  <div class="abs hero-art" role="img" aria-label="Illustration of a head silhouette with gears and speech bubbles of knowledge icons"></div>

  <main class="abs main"></main>
  <h2 class="abs intro-title">Welcome to Our Website</h2>
  <p class="abs intro-copy">But I must explain to you how all this mistaken idea of denouncing pleasure and praising pain was born and I will give you a complete account of the system, and expound the actual teachings of the great explorer of the truth, the master-builder of human happiness. No one rejects, dislikes, or avoids pleasure itself, because it is pleasure, but because those who do not know how to pursue pleasure rationally encounter consequences that are extremely painful.</p>
  <div class="abs btn-orange read-more">Read more</div>
  <div class="abs video">
    <div class="video-screen" role="img" aria-label="Video still of a psychic speaking">
      <span class="video-play"></span>
      <span class="video-caption">Can you be psychic?</span>
    </div>
  </div>

  <section class="abs card" style="left:88px;top:656px;width:266px;height:330px">
    <h3 class="card-head">Top Physics</h3>
    <div class="arrows"><i></i><i></i></div>
    <div class="entry" style="top:40px"><p><b>Lorem ipsum dolor sit amet, consectetur</b> adipisicing elit, sed do eiusmod tempor incididunt ut labore et dolore magna aliqua. Ut enim ad</p><div class="thumb" role="img" aria-label="Portrait photo of a psychic" style="background:linear-gradient(#7a4a2a,#c9a089)"></div><span class="view-more">View more</span></div>
    <div class="entry" style="top:136px"><p><b>Lorem ipsum dolor sit amet, consectetur</b> adipisicing elit, sed do eiusmod tempor incididunt ut labore et dolore magna aliqua. Ut enim ad</p><div class="thumb" role="img" aria-label="Photo of two psychics outdoors" style="background:linear-gradient(#3f7a3a,#1f3a2a)"></div><span class="view-more">View more</span></div>
    <div class="entry" style="top:240px"><p><b>Lorem ipsum dolor sit amet, consectetur</b> adipisicing elit, sed do eiusmod tempor incididunt ut labore et dolore magna aliqua. Ut enim ad</p><div class="thumb" role="img" aria-label="Portrait photo of a psychic" style="background:linear-gradient(#f2f2f2,#6a5040)"></div><span class="view-more">View more</span></div>
  </section>

  <section class="abs card" style="left:361px;top:656px;width:265px;height:330px">
    <h3 class="card-head">What our physician say</h3>
    <div class="arrows"><i></i><i></i></div>
    <div class="entry" style="top:40px"><p><b>Lorem ipsum dolor sit amet, consectetur</b> adipisicing elit, sed do eiusmod tempor incididunt ut labore et dolore magna aliqua. Ut enim ad</p><div class="thumb" role="img" aria-label="Portrait photo of a customer" style="background:linear-gradient(#d8b8a0,#8a5a3a)"></div><span class="view-more">View more</span></div>
    <div class="entry" style="top:136px"><p><b>Lorem ipsum dolor sit amet, consectetur</b> adipisicing elit, sed do eiusmod tempor incididunt ut labore et dolore magna aliqua. Ut enim ad</p><div class="thumb" role="img" aria-label="Portrait photo of a customer" style="background:linear-gradient(#7a7a7a,#c49a7c)"></div><span class="view-more">View more</span></div>
    <div class="entry" style="top:240px"><p><b>Lorem ipsum dolor sit amet, consectetur</b> adipisicing elit, sed do eiusmod tempor incididunt ut labore et dolore magna aliqua. Ut enim ad</p><div class="thumb" role="img" aria-label="Portrait photo of a customer" style="background:linear-gradient(#f5f5f5,#8a6a55)"></div><span class="view-more">View more</span></div>
  </section>

  <aside class="abs card" style="left:639px;top:652px;width:184px;height:178px">
    <h3 class="side-title">Daily Newsletter Finds</h3>
    <p class="side-copy">Mauris vel lacus vitae felis vestibu-lum Etiam est nunc</p>
    <div class="side-input"></div>
    <div class="btn-orange signup">Sign Up</div>
    <p class="side-note">See our more newsletters here.</p>
  </aside>

  <aside class="abs card" style="left:639px;top:846px;width:184px;height:176px">
    <h3 class="side-title">Physics Market Place</h3>
    <div class="item" style="left:16px"><div class="pic" role="img" aria-label="Love spell product image"></div><div class="name">Love Spell</div><div class="price">$200.00</div></div>
    <div class="item" style="left:100px"><div class="pic" role="img" aria-label="Candle spell product image" style="background:radial-gradient(circle,#fff 0%,#c8102e 45%,#111 100%)"></div><div class="name">Love Spell</div><div class="price">$200.00</div></div>
  </aside>

  <h3 class="abs products-title">OUR PRODUCTS</h3>
  <div class="abs products-arrows"><i></i><i></i></div>
  <div class="abs product" style="left:90px"><div role="img" aria-label="Hands building a molecular model" style="background:linear-gradient(135deg,#c9a890,#e6e0dc)"></div></div>
  <div class="abs product" style="left:198px"><div role="img" aria-label="Engine teaching model" style="background:linear-gradient(135deg,#f2f2f2,#3a6aa8 60%,#c84a2a)"></div></div>
  <div class="abs product" style="left:306px"><div role="img" aria-label="Lab instrument" style="background:linear-gradient(135deg,#e8e8e8,#9a9a9a)"></div></div>
  <div class="abs product" style="left:414px"><div role="img" aria-label="Open equipment case" style="background:linear-gradient(135deg,#dcdcdc,#2a2a2a)"></div></div>
  <div class="abs product" style="left:522px"><div role="img" aria-label="Lab device with red light" style="background:linear-gradient(135deg,#9a8a7a,#e0d8d4 60%,#c86a6a)"></div></div>

  <footer class="abs footer"></footer>
  <nav class="abs footer-links">
    <span>Home</span><span>|</span><span>Psychic</span><span>|</span><span>Marketplace</span><span>|</span><span>Psychic profile</span><span>|</span><span>Psychic Store</span><span>|</span><span>Psychic product</span><span>|</span><span>Sign in</span><span>|</span><span>Register</span>
  </nav>
  <p class="abs copyright">Copyright © &nbsp;2013 &nbsp;www.lanternofseers-demo.net &nbsp;&nbsp;All rights reserved.</p>
  <div class="abs social">
    <i></i><i></i><i></i>
    <i><svg width="22" height="22" viewBox="0 0 22 22"><rect x="5.5" y="7" width="11" height="8" fill="none" stroke="#fff" stroke-width="1.2"/><path d="M5.5 7l5.5 5 5.5-5" fill="none" stroke="#fff" stroke-width="1.2"/></svg></i>
  </div>

</div>
</body>
</html>
```